Business Card Design for Fashion Tech Startup

Dear designers, we need a business card for Asia's premier fashion tech startup.!

PebbleNest is discovery e-commerce destination for busy, discerning parents in Asia featuring leading independent designers of baby, kids fashion apparel and sustainable brands from around the world.

PebbleNest is a modern, contemporary fashion tech startup targeting well-educated, well travelled and affluent parents. We're NOT your typical kiddy store!! Our design philosophy & e-commerce site is more like Vorn.com, Quenibo.com, Darwick.com, Tamsfield.com.
Updates

Hi, size of the business card should be 84mm X 55mm. Would appreciate some business card layouts in Portrait as added consideration, i fancy the idea of a Portrait business card. What's important is that the business card should pique the receiver's interest to log onto the website to learn more. Many thanks and love forward to the designs!

Target Market(s)

Though modern, classy in look, feel & positioning, PebbleNest does possess a cheeky, fun-loving personality as depicted by its logo and the segment it targets (baby, kids) though the key decision makers i.e primarily mums between 25-40 who are well educated/travelled, local & expatriates, internet/digitally savvy, mid-high income working mums.

Industry/Entity Type

E-Commerce

Requirements
Must have
• Name, designation, email, phone & mobile number.
Company url : www.pebblenest.sg
Slogan : Discovery e-commerce destination for discerning, busy parents
Nice to have
• Call to Action such as a Discount code offering 10% discount
or asking people to "Like" us on our Fanwall page/Fanwall URL

```html
<!DOCTYPE html>
<html lang="en">
<head>
<meta charset="utf-8">
<title>PebbleNest Business Card</title>
<link rel="stylesheet" href="https://fonts.googleapis.com/css2?family=Josefin+Sans:wght@100;300;400;600&family=Open+Sans:wght@400;600&display=swap">
<style>
  :root {
    --backdrop: #2a2a2c;
    --card-white: #ffffff;
    --navy: #3b5e77;
    --navy-deep: #2f4f66;
    --navy-soft: #456b85;
    --coral: #ef6f5c;
    --ink: #3b5e77;
    --rule: #b9c6d0;
    --faint: #f1f3f6;
  }
  * { box-sizing: border-box; margin: 0; padding: 0; }
  html, body { width: 1200px; height: 900px; overflow: hidden; }
  body {
    background: var(--backdrop);
    font-family: "Josefin Sans", sans-serif;
    position: relative;
  }
  .card {
    position: absolute;
    top: 130px;
    width: 419px;
    height: 640px;
    overflow: hidden;
  }
  .card--front { left: 141px; background: var(--card-white); }
  .card--back { left: 640px; background: var(--navy); color: #fff; }

  .brand {
    position: absolute;
    display: flex;
    align-items: center;
    gap: 14px;
  }
  .brand__dot {
    width: 58px; height: 58px; border-radius: 50%;
    flex: none;
  }
  .brand__name {
    font-family: "Josefin Sans", sans-serif;
    font-weight: 600;
    font-size: 38px;
    letter-spacing: 0.5px;
  }
  .card--front .brand { left: 56px; top: 170px; }
  .card--front .brand__dot { background: var(--navy); }
  .card--front .brand__name { color: var(--coral); }

  .front__halo {
    position: absolute; right: -70px; top: 30px;
    width: 300px; height: 300px; border-radius: 50%;
    background: var(--faint);
  }

  .contact { position: absolute; left: 34px; right: 34px; top: 360px; color: var(--ink); }
  .contact__name {
    font-weight: 100; font-size: 50px; letter-spacing: 4px;
    text-transform: uppercase; line-height: 1;
  }
  .contact__title-row { display: flex; align-items: center; gap: 10px; margin-top: 6px; }
  .contact__rule { flex: 1; height: 1px; background: var(--rule); }
  .contact__title { font-weight: 300; font-size: 20px; letter-spacing: 5px; }
  .contact__details {
    margin-top: 22px; font-family: "Open Sans", sans-serif;
    font-size: 14px; letter-spacing: 0.5px; text-align: center;
  }
  .contact__divider { height: 1px; background: var(--rule); margin: 12px 0; }
  .contact__web {
    font-weight: 300; font-size: 17px; letter-spacing: 8px; text-align: center;
  }

  .front__band {
    position: absolute; left: 0; right: 0; bottom: 52px; height: 58px;
    background: var(--navy); color: #fff;
    display: flex; align-items: center; justify-content: center;
    font-family: "Open Sans", sans-serif; font-size: 16px; letter-spacing: 0.5px;
  }
  .front__band-edge {
    position: absolute; left: 0; right: 0; bottom: 36px; height: 6px;
    background: var(--navy);
  }

  .back__pattern {
    position: absolute; inset: 0;
    background: radial-gradient(circle at 40% 40%, var(--navy-soft), var(--navy) 60%, var(--navy-deep));
  }
  .card--back .brand { left: 60px; top: 190px; }
  .card--back .brand__dot { background: #fff; }
  .card--back .brand__name { color: #fff; }
  .back__slogan {
    position: absolute; left: 40px; right: 40px; top: 272px;
    text-align: center; font-family: "Open Sans", sans-serif;
    font-size: 15px; line-height: 1.45;
  }
  .back__web {
    position: absolute; left: 0; right: 0; bottom: 120px;
    text-align: center; font-family: "Open Sans", sans-serif;
    font-size: 19px; letter-spacing: 5px;
  }
</style>
</head>
<body>
  <section class="card card--front">
    <div class="front__halo"></div>
    <div class="brand">
      <span class="brand__dot"></span>
      <span class="brand__name">PebbleNest</span>
    </div>
    <div class="contact">
      <h1 class="contact__name">Ella Marsh</h1>
      <div class="contact__title-row">
        <span class="contact__rule"></span>
        <span class="contact__title">President</span>
        <span class="contact__rule" style="flex:0 0 30px"></span>
      </div>
      <p class="contact__details">t. 012-555-0147 &bull; e. ella@pebblenest.sg</p>
      <div class="contact__divider"></div>
      <p class="contact__web">www.pebblenest.sg</p>
      <div class="contact__divider"></div>
    </div>
    <div class="front__band">&ldquo;Like&rdquo; us on our Fanwall</div>
    <div class="front__band-edge"></div>
  </section>

  <section class="card card--back">
    <div class="back__pattern" role="img" aria-label="Tonal pattern of baby items and toys in navy blue"></div>
    <div class="brand">
      <span class="brand__dot"></span>
      <span class="brand__name">PebbleNest</span>
    </div>
    <p class="back__slogan">Discovery e-commerce destination<br>for discerning, busy parents</p>
    <p class="back__web">www.pebblenest.sg</p>
  </section>
</body>
</html>
```